1 Page for Computer Repair Website

Looking for a 1 page website with a design that compliments the business card and pamphlet that have already been made (attached files). It should look business professional and easy to read. Email and phone number should be somewhere near the top of the website, visible when the page loads. I don't want any forms for people to mess with. No "Contact Us" form or entering in email for newsletter. Customers will just be looking at this site to confirm we are professionals and have our business in order.

Target Market(s)

Home and small business

Industry/Entity Type

Computer Repair

Coding

Coded - Design and coding required

Number of Pages Required

1 page

Font styles to use
Other font styles liked:
• Helvetica variations used in pamphlet and card

Colors
0455a3
cfdeed
85abd2
3276b5
85cae6
ffffff

Requirements
Must have
• Compliment the pamphlet and business card in color choices and font use. Pleasing to the eye and easy to read through categories and text.
Should not have
• Forms. No "enter name and email here" or anything of the sort.

```html
<!DOCTYPE html>
<html lang="en">
<head>
<meta charset="utf-8">
<title>Quickbyte Computer Services</title>
<link href="https://fonts.googleapis.com/css2?family=Open+Sans:wght@400;600;700;800&display=swap" rel="stylesheet">
<style>
:root{
  --blue:#0455a3;
  --blue-mid:#3276b5;
  --blue-soft:#85abd2;
  --sky:#85cae6;
  --ice:#cfdeed;
  --white:#ffffff;
  --ink:#222a33;
  --text:#6b7480;
  --grey-bg:#f1f2f4;
  --navy:#1e2733;
  --navy-deep:#161d27;
}
*{box-sizing:border-box;margin:0;padding:0}
html,body{width:1200px;height:2536px;overflow:hidden}
body{font-family:"Open Sans",Helvetica,Arial,sans-serif;color:var(--text);background:var(--white);position:relative}
section,header,footer,div{position:relative}
.abs{position:absolute}
p{font-size:13px;line-height:20px}

.topbar{height:36px;background:#f7f7f7;border-bottom:1px solid #e4e4e4;font-size:11px;display:flex;justify-content:space-between;align-items:center;padding:0 140px}
.topbar strong{color:var(--blue)}
.login{display:flex;align-items:center;gap:6px}
.login span{width:10px;height:10px;background:var(--blue-soft);display:inline-block}

.site-header{height:64px;display:flex;justify-content:space-between;align-items:center;padding:0 140px;border-bottom:1px solid #eee}
.brand{display:flex;align-items:center}
.brand-name{font-size:26px;font-weight:700;color:var(--blue);line-height:1}
.nav{display:flex;gap:10px}
.nav a{font-size:11px;font-weight:600;color:var(--ink);text-decoration:none;padding:6px 14px;border-radius:3px}
.nav a.active{background:var(--blue);color:var(--white)}

.hero{height:420px;background:linear-gradient(90deg,#eef0f2,#e3e6e9)}
.hero-photo{left:640px;top:0;width:560px;height:420px;background:linear-gradient(120deg,#d9dde2,#b9c3cc 55%,#8ea2b4)}
.hero-copy{left:140px;top:112px;width:470px}
.hero h1{font-size:26px;font-weight:800;color:var(--ink);line-height:34px;white-space:nowrap}
.hero h1 em{font-style:normal;color:var(--blue);display:block}
.hero p{margin-top:12px;font-size:12px;line-height:18px;width:430px}
.btn{display:inline-block;background:var(--blue);color:var(--white);font-size:11px;font-weight:700;padding:9px 20px;border-radius:18px;margin-top:18px;letter-spacing:.5px}

.about{height:600px}
.about-copy{left:140px;top:72px;width:460px}
.section-title{font-size:30px;font-weight:800;color:var(--ink)}
.about h3{font-size:22px;font-weight:600;color:var(--blue);margin:2px 0 14px}
.about p+p{margin-top:14px}
.about-device{left:640px;top:60px;width:500px;height:400px;background:linear-gradient(160deg,#f2f4f6,#c9d2db);border-radius:6px}

.services{height:440px;background:var(--grey-bg);text-align:center}
.services .section-title,.why .section-title{padding-top:54px}
.lead{width:820px;margin:14px auto 0;font-size:12px;line-height:18px}
.service-line{left:190px;top:214px;width:820px;height:1px;background:#c9ccd1}
.arrow{top:196px;width:36px;height:36px}
.services-row{display:flex;justify-content:space-between;width:820px;margin:40px auto 0}
.service{width:200px}
.icon-circle{width:64px;height:64px;border-radius:50%;background:var(--blue);margin:0 auto;display:flex;align-items:center;justify-content:center;box-shadow:0 0 0 6px var(--grey-bg)}
.service h4{font-size:17px;font-weight:700;color:var(--ink);margin-top:16px}
.service p{font-size:11px;line-height:16px;margin-top:6px}

.why{height:580px;text-align:center}
.why-list{left:150px;top:210px;width:370px;text-align:left}
.why-item{display:flex;align-items:center;margin-bottom:26px}
.why-item .icon-circle{width:56px;height:56px;margin:0;box-shadow:none;flex:none}
.why-item div.box{background:#f0f1f3;flex:1;margin-left:-4px;padding:12px 16px;font-size:11px;line-height:16px}
.why-device{left:540px;top:200px;width:560px;height:350px;background:linear-gradient(150deg,#dfe6ee,#8fa9c2 60%,#5f7f9f);border-radius:6px}

.site-footer{height:340px;background:var(--navy);color:#a7b0bc}
.foot-col{top:60px}
.foot-col h5{font-size:15px;font-weight:700;color:var(--white);margin-bottom:18px}
.foot-col li{list-style:none;font-size:11px;line-height:22px}
.foot-col li::before{content:"›  ";color:var(--sky)}
.foot-col p{font-size:11px;line-height:17px}
.social{display:flex;gap:6px;margin-top:14px}
.social span{width:22px;height:22px;border:1px solid #4a5566;display:block}
.bottombar{height:56px;background:var(--navy-deep);color:#8a94a2;font-size:11px;display:flex;justify-content:space-between;align-items:center;padding:0 150px}
</style>
</head>
<body>

<div class="topbar">
  <span>Do you have any questions? Call us: <strong>+00 (12) 456 7890</strong> or email: <strong>help@quickbyte-example.com</strong></span>
  <span class="login"><span></span>Login</span>
</div>

<header class="site-header">
  <div class="brand"><span class="brand-name">Quickbyte</span></div>
  <nav class="nav">
    <a class="active">HOME</a><a>ABOUT US</a><a>OUR SERVICES</a><a>WHY CHOOSE US</a><a>CONTACT US</a>
  </nav>
</header>

<section class="hero">
  <div class="abs hero-photo" role="img" aria-label="Technician in a lab coat repairing an open desktop computer"></div>
  <div class="abs hero-copy">
    <h1>WELCOME TO<em>QUICKBYTE COMPUTER SERVICES</em></h1>
    <p>We repair, clean and upgrade home and office computers with care. Fast turnaround, honest pricing and friendly advice from certified technicians who explain every step before starting work.</p>
    <span class="btn">LEARN MORE</span>
  </div>
</section>

<section class="about">
  <div class="abs about-copy">
    <h2 class="section-title">ABOUT US</h2>
    <h3>We are passionate in what we do.</h3>
    <p>Our team has served local homes and small businesses for years, fixing laptops, desktops and networks. We focus on clear communication, careful diagnosis and lasting repairs so your equipment keeps working when you need it most.</p>
    <p>Every job is tracked from drop off to pick up. We test thoroughly, back up what matters and only recommend parts that make sense for your budget and goals.</p>
    <span class="btn">LEARN MORE</span>
  </div>
  <div class="abs about-device" role="img" aria-label="Laptop displaying a news website, a hand reaching toward the screen"></div>
</section>

<section class="services">
  <h2 class="section-title">OUR SERVICES</h2>
  <p class="lead">From a slow laptop to a failed office server, we handle the full range of computer problems. Choose a service below or call us for a quick diagnosis and a clear quote before any work begins.</p>
  <div class="abs service-line"></div>
  <svg class="abs arrow" style="left:110px" viewBox="0 0 36 36"><path d="M22 8 12 18l10 10" fill="none" stroke="#222a33" stroke-width="3"/></svg>
  <svg class="abs arrow" style="left:1054px" viewBox="0 0 36 36"><path d="M14 8l10 10-10 10" fill="none" stroke="#222a33" stroke-width="3"/></svg>
  <div class="services-row">
    <div class="service">
      <div class="icon-circle"><svg width="28" height="28" viewBox="0 0 24 24"><path d="M12 2 4 5v6c0 5 3.5 9 8 11 4.5-2 8-6 8-11V5z" fill="none" stroke="#fff" stroke-width="2"/></svg></div>
      <h4>Malware Removal</h4>
      <p>Viruses and spyware removed safely, with your files kept intact.</p>
    </div>
    <div class="service">
      <div class="icon-circle"><svg width="28" height="28" viewBox="0 0 24 24"><rect x="3" y="4" width="18" height="12" rx="1" fill="none" stroke="#fff" stroke-width="2"/><path d="M8 20h8M12 16v4" stroke="#fff" stroke-width="2"/></svg></div>
      <h4>PC / Laptop</h4>
      <p>Screens, keyboards, batteries and boards repaired or replaced.</p>
    </div>
    <div class="service">
      <div class="icon-circle"><svg width="28" height="28" viewBox="0 0 24 24"><rect x="3" y="6" width="18" height="12" rx="2" fill="none" stroke="#fff" stroke-width="2"/><circle cx="17" cy="12" r="1.5" fill="#fff"/></svg></div>
      <h4>Hard/Software</h4>
      <p>Upgrades, installs and setup for the tools your work needs.</p>
    </div>
    <div class="service">
      <div class="icon-circle"><svg width="28" height="28" viewBox="0 0 24 24"><ellipse cx="12" cy="5" rx="7" ry="3" fill="none" stroke="#fff" stroke-width="2"/><path d="M5 5v14c0 1.7 3.1 3 7 3s7-1.3 7-3V5M5 12c0 1.7 3.1 3 7 3s7-1.3 7-3" fill="none" stroke="#fff" stroke-width="2"/></svg></div>
      <h4>Data Immigration</h4>
      <p>Files moved to new machines quickly, securely and completely.</p>
    </div>
  </div>
</section>

<section class="why">
  <h2 class="section-title">WHY CHOOSE US</h2>
  <p class="lead">Local, trusted and straightforward. We treat every device as if it were our own and stand behind our work with a clear warranty on parts and labour for every repair we complete.</p>
  <div class="abs why-list">
    <div class="why-item"><div class="icon-circle"><svg width="24" height="24" viewBox="0 0 24 24"><rect x="3" y="5" width="18" height="12" fill="none" stroke="#fff" stroke-width="2"/><path d="M9 20h6" stroke="#fff" stroke-width="2"/></svg></div><div class="box">Certified technicians with years of hands-on repair <strong>industry</strong> experience.</div></div>
    <div class="why-item"><div class="icon-circle"><svg width="24" height="24" viewBox="0 0 24 24"><path d="M5 12l4 4 10-10" fill="none" stroke="#fff" stroke-width="2.5"/></svg></div><div class="box">Free diagnosis and honest quotes before any <strong>industry</strong> standard work.</div></div>
    <div class="why-item"><div class="icon-circle"><svg width="24" height="24" viewBox="0 0 24 24"><circle cx="12" cy="12" r="8" fill="none" stroke="#fff" stroke-width="2"/><path d="M12 7v5l3 2" stroke="#fff" stroke-width="2" fill="none"/></svg></div><div class="box">Quick turnaround on most repairs, often the same <strong>industry</strong> day.</div></div>
    <div class="why-item"><div class="icon-circle"><svg width="24" height="24" viewBox="0 0 24 24"><path d="M6.6 10.8a15 15 0 0 0 6.6 6.6l2.2-2.2c.3-.3.7-.4 1-.2 1.1.4 2.3.6 3.6.6v4c-9.4 0-17-7.6-17-17h4c0 1.3.2 2.5.6 3.6.1.3 0 .7-.2 1z" fill="#fff"/></svg></div><div class="box">Friendly support by phone after every repair we <strong>industry</strong> complete.</div></div>
  </div>
  <div class="abs why-device" role="img" aria-label="Laptop showing a smiling team of technicians in an office"></div>
</section>

<footer class="site-footer">
  <div class="abs foot-col" style="left:150px;width:240px">
    <h5>NEWSLETTER SUBSCRIBE</h5>
    <p>Tips on keeping your computer fast and safe, shared in store and by phone.</p>
  </div>
  <div class="abs foot-col" style="left:430px">
    <h5>QUICK LINKS</h5>
    <ul><li>Home</li><li>About Us</li><li>Why Choose Us</li><li>Testimonials</li><li>Contact Us</li></ul>
  </div>
  <div class="abs foot-col" style="left:640px">
    <h5>INDUSTRY SOLUTION</h5>
    <ul><li>Laptop Repairs</li><li>Virus Removal</li><li>Data Loss</li><li>Hard Drives</li><li>Upgrades</li><li>Network Setup</li></ul>
  </div>
  <div class="abs foot-col" style="left:880px;width:180px">
    <h5>CONTACT US</h5>
    <p>123 Example Street<br>Sample City, ST 00000<br>+00 12 456 7890<br>help@quickbyte-example.com</p>
    <div class="social"><span></span><span></span><span></span></div>
  </div>
</footer>
<div class="bottombar"><span>Copyright © 2024 Quickbyte, Inc. All Rights Reserved</span><span>Terms &amp; Conditions &nbsp;|&nbsp; Privacy Policy</span></div>

</body>
</html>
```